July 2022 Industrial Manufacturer Product Expo Mexico City

We manufacture large screws and fastners for large Mining equipment, Trains, large ships, airplanes, wind turbines, and so on. We also do custom work base on the customer needs. No matter the size we can make it.
We have a Expo coming up with companies all over the world. We have to stand out we are a family own business so our customer service will be above and beyond anyone can provide. We do not have a sales force to push our products and services we provide one on one service.
Plus@!! I'm looking for anything that you designers can come up with if it was your company to put on a business card, plus i want to do a 1 or 2 sided pamphlet, and then a website. We make Speciality Bolts for large mining equipment these bolts can be 3 to 4 foot long!!! Plus fasteners, Nuts, washers, any, size, strengths, special materials, we offer more of a ono on one customer service, We are a small company, family own, but can fulfill any type of orders. We can also provide special time lines for emergency orders. "We keep the machines running we here at KRV don't believe in down time" We want to hear any slogan based on our company to stand out.
Thanks i really appreciate all your work and options that we have to pick on. Plus just a thought we could possibly want to entertain a experience Marketing internet help maybe a employment possibility. Thanks
Updates

I need 2 cards one in Spanish and English Like the steel back ground maybe send me in some bright red and blue writing Same with the Black cards Please remove the word Military The logo KRV maybe integrate a picture of a Bolt 🔩 Thank you

Still looking for I need 2 cards one in Spanish and English Like the steel back ground maybe send me in some bright red and blue writing Same with the Black cards try bright writing Please remove the word Military The logo KRV maybe integrate a picture of a Bolt 🔩 Plus will need the company to make a brochure and website next Thank you

Target Market(s)

Large Mining, Ship, Train, Green Energy, ORBA, and Government equipment. Throughout the World

Industry/Entity Type

We can Custom Manufacture any type of Fastners for Mining equipment, Trains, Ships, Green energy, Governments, or military projects. wind turbines,

Contact Information for Business Card

I attached the name and contact info that's on a card, plus the Company Logo. Would like industrial looking background with Bright Colors that will stand out!! If we can insert somewhere maybe on back that we "Custom Manufacture Any Size or Quantity Fastners for Large Mining Equipment, Trains, Ships, Green Energy Equipment or Government Projects

Font styles to use
Other font styles liked:
• You Pick, has to be bold, colorful standout, Professional looking Beable to read it.

Colors

Designer to choose colors to be used in the design.

Requirements
Must have
• Need in Spanish and English TO STANDOUT FROM THE REST OF THE EXPO!! See Business card details, Rounded corners
Nice to have
• Can i see some of the darker cards with Bright Red and Blue letters I like to see the different type of card material, heavy thickness, plastic, transparent, Metal types, Bright Colors, I saw like Raised letters like on the logo.

```html
<!DOCTYPE html>
<html lang="es">
<head>
<meta charset="utf-8">
<title>KRV Business Cards</title>
<link href="https://fonts.googleapis.com/css2?family=Quicksand:wght@500;600;700&display=swap" rel="stylesheet">
<style>
  :root{
    --backdrop:#2b2b2d;
    --steel-dark:#6f7175;
    --steel-mid:#a4a6aa;
    --steel-light:#eceef0;
    --ink-blue:#0c5f93;
    --bright-blue:#2fb0ea;
    --logo-gray:#3a3b3e;
  }
  *{margin:0;padding:0;box-sizing:border-box}
  html,body{width:1200px;height:900px;overflow:hidden}
  body{background:var(--backdrop);font-family:"Quicksand",sans-serif;position:relative}
  .card{
    position:absolute;width:600px;height:343px;border-radius:34px;overflow:hidden;
    background:linear-gradient(100deg,var(--steel-dark) 0%,var(--steel-mid) 22%,var(--steel-dark) 38%,var(--steel-mid) 55%,var(--steel-light) 70%,var(--steel-mid) 84%,var(--steel-dark) 100%);
    box-shadow:0 18px 40px rgba(0,0,0,.55);
  }
  .card--front{left:140px;top:70px}
  .card--back{left:460px;top:487px}
  .brand-name{
    position:absolute;font-weight:700;font-size:76px;letter-spacing:8px;color:var(--logo-gray);line-height:1;
  }
  .card--front .brand-name{left:0;right:0;top:48px;text-align:center}
  .card--back .brand-name{right:70px;top:42px}
  .tagline{
    position:absolute;left:40px;right:40px;top:168px;text-align:center;
    color:var(--ink-blue);font-weight:700;font-size:19px;line-height:1.45;
  }
  .holder{position:absolute;left:46px;top:158px}
  .holder__name{color:var(--bright-blue);font-weight:700;font-size:25px}
  .holder__role{color:var(--bright-blue);font-weight:600;font-size:17px;margin-top:2px}
  .contact-list{position:absolute;left:92px;top:248px;list-style:none}
  .contact-list li{display:flex;align-items:center;gap:10px;color:var(--bright-blue);font-weight:600;font-size:17px;line-height:1.55}
  .contact-list svg{width:16px;height:16px;flex:none}
</style>
</head>
<body>
  <section class="card card--front" aria-label="Card front">
    <div class="brand-name">KRV</div>
    <p class="tagline">Custom Manufacture Any Size or<br>Quantity Fastners for Large Mining Equipment<br>Trains, Ships, Green Energy Equipment<br>or Government Projects</p>
  </section>

  <section class="card card--back" aria-label="Card back">
    <div class="brand-name">KRV</div>
    <div class="holder">
      <div class="holder__name">Lic. Daniela Moreno Ríos</div>
      <div class="holder__role">Cotizaciones en</div>
    </div>
    <ul class="contact-list">
      <li>
        <svg viewBox="0 0 16 16" aria-hidden="true"><path fill="#2fb0ea" d="M2 5c0-2 2-3 6-3s6 1 6 3v1h-3V5H5v1H2zM4 7h8l2 6H2z"/></svg>
        871 555 0142
      </li>
      <li>
        <svg viewBox="0 0 16 16" aria-hidden="true"><rect x="4" y="1" width="8" height="14" rx="1.5" fill="none" stroke="#2fb0ea" stroke-width="1.5"/></svg>
        8715550187
      </li>
      <li>
        <svg viewBox="0 0 16 16" aria-hidden="true"><rect x="1" y="3" width="14" height="10" rx="1.5" fill="#2fb0ea"/><path d="M1.5 4l6.5 5 6.5-5" fill="none" stroke="#fff" stroke-width="1.2"/></svg>
        ventas.krv@correo.mx
      </li>
    </ul>
  </section>
</body>
</html>
```